Velvet Harbor for sale at the 2019 Tandor Crest Mare Auction on 30 May 2019

I am selling my broodmare at the 2019 Tandor Crest Mare auction on 30 May 2019. I need a flyer to hand out to potential buyers. I have included the required information in the attached word document. I can provide more images if required. I am thinking that a DL double sided or an A5 will suit best. I'm happy to provide more information as required.

Target Market(s)

Race horse breeders, people who buy broodmares.

Font styles to use
Serif
Sans Serif
Script

Colors

Designer to choose colors to be used in the design.

Requirements
Must have
• All of the content provided in the attached brief, however it is not necessary to have the words exactly as per the brief. The brief is for information purposes.
Nice to have
• Innovation...

```html
<!DOCTYPE html>
<html lang="en">
<head>
<meta charset="UTF-8">
<title>Velvet Harbor – Tandor Crest Mare Auction</title>
<link rel="stylesheet" href="https://fonts.googleapis.com/css2?family=Bungee&family=Poppins:ital,wght@0,400;0,500;0,700;1,700;1,800&display=swap">
<style>
  :root {
    --red: #ee3239;
    --white: #ffffff;
    --yellow: #fbbb2a;
    --orange: #f4853f;
    --horse-dark: #1d1516;
    --horse-mid: #3a2a2c;
  }
  html, body {
    margin: 0;
    padding: 0;
    overflow: hidden;
    background: var(--red);
  }
  .flyer {
    position: relative;
    width: 846px;
    height: 1200px;
    overflow: hidden;
    background: var(--red);
    color: var(--white);
    font-family: "Poppins", sans-serif;
  }
  .stripes {
    position: absolute;
    inset: 0;
  }
  .title {
    position: absolute;
    left: 0;
    right: 0;
    top: 62px;
    margin: 0;
    text-align: center;
    font-family: "Bungee", sans-serif;
    font-weight: 400;
    font-size: 78px;
    line-height: 1.2;
    letter-spacing: 1px;
  }
  .lineage {
    position: absolute;
    right: 60px;
    top: 156px;
    margin: 0;
    font-style: italic;
    font-weight: 800;
    font-size: 23px;
  }
  .horse-photo {
    position: absolute;
    left: 60px;
    top: 214px;
    width: 660px;
    height: 510px;
    border-radius: 42% 38% 46% 40% / 30% 34% 60% 58%;
    background: radial-gradient(ellipse at 45% 40%, var(--horse-mid), var(--horse-dark) 72%);
  }
  .lot-badge {
    position: absolute;
    left: 535px;
    top: 195px;
    width: 324px;
    height: 324px;
    border-radius: 50%;
    background: linear-gradient(135deg, var(--yellow), var(--orange));
  }
  .lot-info {
    position: absolute;
    left: 600px;
    top: 252px;
    width: 202px;
    text-align: center;
  }
  .lot-info .label {
    display: block;
    font-size: 19px;
    font-weight: 500;
    line-height: 24px;
  }
  .lot-info .value {
    display: block;
    font-size: 31px;
    font-weight: 800;
    font-style: italic;
    line-height: 36px;
    margin: 2px 0 12px;
  }
  .detail {
    position: absolute;
    left: 58px;
    display: flex;
    gap: 44px;
  }
  .detail svg { flex: none; margin-top: 2px; }
  .detail h2 {
    margin: 0;
    font-size: 28px;
    font-weight: 800;
    font-style: italic;
    line-height: 34px;
  }
  .detail p {
    margin: 0;
    font-size: 19.5px;
    font-weight: 500;
    line-height: 29px;
  }
  .detail-date { top: 752px; }
  .detail-sale { top: 837px; }
  .pedigree {
    position: absolute;
    left: 58px;
    top: 970px;
    width: 450px;
    margin: 0;
    font-size: 19.5px;
    font-weight: 500;
    line-height: 30px;
  }
  .pedigree strong { font-weight: 700; }
  .record {
    position: absolute;
    left: 533px;
    top: 895px;
    width: 290px;
    height: 290px;
    box-sizing: border-box;
    border: 3px solid var(--white);
    border-radius: 50%;
    background: radial-gradient(circle at 50% 40%, var(--yellow), var(--orange) 75%);
    text-align: center;
  }
  .record h2 {
    margin: 44px 0 8px;
    font-size: 28px;
    font-weight: 800;
    font-style: italic;
    line-height: 34px;
  }
  .record p {
    margin: 0;
    font-size: 19.5px;
    font-weight: 500;
    line-height: 29px;
  }
</style>
</head>
<body>
<main class="flyer">
  <svg class="stripes" width="846" height="1200" viewBox="0 0 846 1200" aria-hidden="true">
    <defs>
      <linearGradient id="stripeFill" x1="0" y1="0" x2="1" y2="1">
        <stop offset="0" stop-color="#fbbb2a"/>
        <stop offset="1" stop-color="#f4853f"/>
      </linearGradient>
    </defs>
    <g stroke="url(#stripeFill)" stroke-linecap="round" stroke-width="40" fill="none">
      <line x1="-30" y1="228" x2="676" y2="758"/>
      <line x1="62" y1="378" x2="560" y2="752"/>
      <line x1="-30" y1="445" x2="589" y2="854"/>
    </g>
  </svg>

  <h1 class="title">VELVET HARBOR</h1>
  <p class="lineage">(BY BRIGHTWIND, OUT OF MARLENNA)</p>

  <div class="horse-photo" role="img" aria-label="Photo of the dark bay mare galloping with a jockey in red silks and cap"></div>

  <div class="lot-badge"></div>
  <div class="lot-info">
    <span class="label">LOT NUMBER:</span>
    <span class="value">1414</span>
    <span class="label">STABLE:</span>
    <span class="value">QC 6</span>
  </div>

  <section class="detail detail-date">
    <svg width="48" height="54" viewBox="0 0 50 56" aria-hidden="true">
      <rect x="3" y="8" width="44" height="44" rx="5" fill="none" stroke="#fff" stroke-width="5"/>
      <rect x="3" y="8" width="44" height="10" fill="#fff"/>
      <rect x="11" y="2" width="5" height="11" rx="2" fill="#fff"/>
      <rect x="34" y="2" width="5" height="11" rx="2" fill="#fff"/>
      <g fill="#fff">
        <rect x="12" y="26" width="6" height="6"/><rect x="22" y="26" width="6" height="6"/><rect x="32" y="26" width="6" height="6"/>
        <rect x="12" y="36" width="6" height="6"/><rect x="22" y="36" width="6" height="6"/><rect x="32" y="36" width="6" height="6"/>
      </g>
    </svg>
    <div>
      <h2>SALE DATE:</h2>
      <p>30 May 2019</p>
    </div>
  </section>

  <section class="detail detail-sale">
    <svg width="54" height="52" viewBox="0 0 56 54" aria-hidden="true" fill="none" stroke="#fff" stroke-width="4" stroke-linejoin="round">
      <path d="M4 24 L16 20 L28 26 L40 20 L52 24 L52 50 L40 46 L28 50 L16 46 L4 50 Z"/>
      <path d="M16 20 V46 M40 20 V46"/>
      <path d="M28 34 C20 24 18 18 20 12 A9 9 0 0 1 36 12 C38 18 36 24 28 34 Z" fill="#ee3239"/>
      <circle cx="28" cy="14" r="3"/>
    </svg>
    <div>
      <h2>SALE:</h2>
      <p>2019 Tandor Crest Mare<br>Auction</p>
    </div>
  </section>

  <p class="pedigree">In foal to <strong>Far Meadow</strong>, sire of: Starline Rush (winner of the Group 3 Coral Bay Stakes by 7.5L), Delve Onward (winner of the Group 2 Ironbark Plate), Harrier Gale (winner of the Tandor Crest Clockwise Classic), Swift Arrow, Nova Sable plus more…</p>

  <section class="record">
    <h2>RACE<br>RECORD:</h2>
    <p>7 wins, 2 seconds,<br>2 thirds (27-7:2:2),<br>$205,400<br>prizemoney</p>
  </section>
</main>
</body>
</html>
```